Design of a Job Advert to inspire people to join our movement

I am looking for a very cool ad to be designed to attract staff to a company. the ad needs to The key objective of this advertisement is to attract Co-creators to join our movement and get an equity share in the platform.

We need to be daring and creative and really get the attention of quality capable resources that can help us to co-create our platform. Which aligns directly with the structure of the company.

The advertisement needs to be very exciting and eye catching. There are key messages that we need to be shown very clearly and needs to pop off the page.

I have attached the ad with all the text changes also I have attached a document that shows the key messages.

I have also included some images from the app for you to use if you feel they will add value.

Can you design an ad that would inspire you personally to be curious to investigate what it is all about.

Something very visually inspiring that is easy to read the key messages.
I will leave it your creative licence.

Thanks and really look forward to seeing the next iteration

Regards Maren

Target Market(s)

Poeple who work for oVax

Requirements
Must have
• Very catching and emotive to move people to understand our movement and join us

```html
<!DOCTYPE html>
<html lang="en">
<head>
<meta charset="utf-8">
<title>AIRVANT – Join the co-creation team</title>
<link href="https://fonts.googleapis.com/css2?family=Montserrat:wght@600;700;800&family=Varela+Round&display=swap" rel="stylesheet">
<style>
:root{
  --sun:#f5c945;
  --amber:#df9a2f;
  --amber-deep:#c9801f;
  --sky:#00b2dd;
  --bubble:#bfe3f0;
  --ink:#231f20;
  --white:#ffffff;
  --screen-dark:#3a3a3a;
  --screen-mid:#777777;
}
*{box-sizing:border-box;margin:0;padding:0}
html,body{width:848px;height:1200px;overflow:hidden;background:var(--white)}
.advert{position:relative;width:848px;height:1200px;overflow:hidden;background:var(--white);font-family:"Varela Round",sans-serif;color:var(--ink)}
.abs{position:absolute}

/* hero */
.hero{left:0;top:0;width:848px;height:380px;background:var(--sun)}
.hero-figures{left:0;top:0;width:360px;height:380px;background:linear-gradient(160deg,var(--amber) 0%,var(--amber-deep) 60%,rgba(223,154,47,0) 100%);opacity:.75;border-radius:0 60% 0 0}
.brand{left:42px;top:112px;display:flex;align-items:center;gap:10px;font-family:"Montserrat",sans-serif;font-weight:700;font-size:28px;letter-spacing:1px;color:var(--white)}
.brand-dot{width:26px;height:26px;border-radius:50%;background:var(--sky)}
.headline{left:42px;top:160px;width:500px;font-family:"Montserrat",sans-serif;font-weight:800;font-size:36px;line-height:35px;color:var(--ink)}
.intro{left:44px;top:286px;width:480px;font-size:16.5px;line-height:20.5px;color:var(--ink)}
.hero-phone{left:574px;top:28px;width:218px;height:352px;border-radius:30px 30px 0 0;background:linear-gradient(180deg,var(--screen-mid),var(--screen-dark));border:6px solid #1c1c1c;border-bottom:none}

/* banner */
.community-banner{left:125px;top:373px;width:598px;height:57px;background:var(--sky);border-radius:0 0 16px 16px;display:flex;align-items:center;justify-content:center;font-family:"Montserrat",sans-serif;font-weight:800;font-size:27px;letter-spacing:2.4px;color:var(--white)}

/* values */
.bubbles{left:560px;top:470px;width:288px;height:385px;background:radial-gradient(circle at 60% 45%,var(--bubble) 0%,rgba(191,227,240,.5) 45%,rgba(191,227,240,0) 75%)}
.app-screens{left:262px;top:450px;width:336px;height:392px;border-radius:26px;background:linear-gradient(135deg,#9a8a7a,#4a4a4a 50%,#7d8fa0)}
.value{font-size:13.5px;line-height:15.5px;color:var(--ink)}
.value.left{left:82px;text-align:left}
.value.right{right:77px;text-align:right}
.rule{height:1.5px;background:var(--ink)}
.rule::after{content:"";position:absolute;top:-1.5px;width:4px;height:4px;border-radius:50%;background:var(--ink)}
.rule.left::after{left:-2px}
.rule.right::after{right:-2px}

/* team */
.team{left:0;top:855px;width:848px;height:243px;background:var(--sun)}
.team-title{left:30px;top:881px;font-family:"Montserrat",sans-serif;font-weight:800;font-size:26px;letter-spacing:1px;color:var(--ink)}
.benefits{left:30px;top:925px;width:600px;list-style:none}
.benefits li{display:flex;align-items:flex-start;gap:14px;font-size:17.5px;line-height:18px;margin-bottom:17px}
.benefits li.wide{margin-bottom:17px}
.tick{flex:none;width:22px;height:22px;margin-top:1px}
.team-phone{left:688px;top:855px;width:160px;height:236px;border-radius:0 0 22px 22px;background:linear-gradient(180deg,#5a5a5a,#8a8a8a 50%,#4a4a4a);border:5px solid #1c1c1c;border-top:none}

/* footer */
.cta{left:30px;top:1120px;width:560px;font-family:"Montserrat",sans-serif;font-weight:600;font-size:18.5px;line-height:26px;color:var(--sky)}
.cta strong{font-weight:700;color:var(--ink);font-size:20px}
.store-badge{top:1108px;width:93px;height:26px;border-radius:4px;background:var(--ink)}
.social{top:1148px;width:35px;height:35px;border-radius:50%;background:var(--ink)}
</style>
</head>
<body>
<main class="advert">

  <section class="abs hero"></section>
  <div class="abs hero-figures" role="img" aria-label="Orange silhouettes of a woman and a man in heroic poses"></div>
  <div class="abs brand"><span class="brand-dot"></span>AIRVANT</div>
  <h1 class="abs headline">The oVax platform that is community built, managed and owned.</h1>
  <p class="abs intro">The world has changed forever, disruption is inevitable and we are looking for the best talent to partner with us through our unique equity participation program.</p>
  <div class="abs hero-phone" role="img" aria-label="App screen inviting users to take an assessment test to unlock their superpowers"></div>

  <div class="abs community-banner">THE AIRVANT COMMUNITY WHERE</div>

  <div class="abs bubbles" role="img" aria-label="Light blue bubble pattern"></div>
  <div class="abs app-screens" role="img" aria-label="Three app screens: profile video, superpower selection menu and a community member video"></div>

  <p class="abs value left" style="top:466px">Users are paid<br>fix their data</p>
  <div class="abs rule left" style="left:76px;top:501px;width:186px"></div>
  <p class="abs value left" style="top:551px">Platform 100%<br>owned by the users</p>
  <div class="abs rule left" style="left:76px;top:586px;width:186px"></div>
  <p class="abs value left" style="top:653px">Democrated Internet of<br>the future is built</p>
  <div class="abs rule left" style="left:76px;top:688px;width:186px"></div>
  <p class="abs value left" style="top:762px">Democrated Internet of<br>the future is built</p>
  <div class="abs rule left" style="left:76px;top:797px;width:268px"></div>

  <p class="abs value right" style="top:466px">Global equality and<br>Fairness are enabled</p>
  <div class="abs rule right" style="left:600px;top:501px;width:180px"></div>
  <p class="abs value right" style="top:551px">Privacy and consent<br>are a right</p>
  <div class="abs rule right" style="left:600px;top:586px;width:180px"></div>
  <p class="abs value right" style="top:638px">Individuals excel and<br>are empowered<br>by the community</p>
  <div class="abs rule right" style="left:598px;top:688px;width:182px"></div>
  <p class="abs value right" style="top:762px">Marekting and<br>Advertising is re-imagined</p>
  <div class="abs rule right" style="left:520px;top:797px;width:260px"></div>

  <section class="abs team"></section>
  <h2 class="abs team-title">BY JOINING OUR TEAM YOU WILL BE</h2>
  <ul class="abs benefits">
    <li class="wide"><svg class="tick" viewBox="0 0 22 22"><path d="M2 12 L8 19 L20 3" fill="none" stroke="#231f20" stroke-width="3" stroke-linecap="round" stroke-linejoin="round"/></svg><span>Instrumental in disrupting the digital world and how the internet is used.</span></li>
    <li><svg class="tick" viewBox="0 0 22 22"><path d="M2 12 L8 19 L20 3" fill="none" stroke="#231f20" stroke-width="3" stroke-linecap="round" stroke-linejoin="round"/></svg><span>Part of a dynamic, ground-breaking team.</span></li>
    <li><svg class="tick" viewBox="0 0 22 22"><path d="M2 12 L8 19 L20 3" fill="none" stroke="#231f20" stroke-width="3" stroke-linecap="round" stroke-linejoin="round"/></svg><span>Challenged and exhilarated.</span></li>
    <li><svg class="tick" viewBox="0 0 22 22"><path d="M2 12 L8 19 L20 3" fill="none" stroke="#231f20" stroke-width="3" stroke-linecap="round" stroke-linejoin="round"/></svg><span>Create substansial value for yourself and your community.</span></li>
  </ul>
  <div class="abs team-phone" role="img" aria-label="App screen listing community members with add buttons"></div>

  <p class="abs cta">Have you the skills, passion and vision to be part of our co-creation team ? email us at <strong>community@airvant.com</strong></p>
  <div class="abs store-badge" style="left:613px"></div>
  <div class="abs store-badge" style="left:720px"></div>
  <div class="abs social" style="left:614px"></div>
  <div class="abs social" style="left:655px"></div>
  <div class="abs social" style="left:695px"></div>
  <div class="abs social" style="left:736px"></div>
  <div class="abs social" style="left:777px"></div>

</main>
</body>
</html>
```